依頼詳細
バランスRスタジオの名刺デザインをお願いします。
楽しく元気のでるイメージで、そこにスタイリッシュさやシンプルな格好良さがあると嬉しいです。
記載項目
屋号:バランスRスタジオ
言葉:〜楽しくキレイと健康を手に入れる〜
代表者:野村 拓海
電話:090−8472−6615
mail:balance.r.studio@hoshimail.jp
住所:栃木県下野市緑ヶ丘412番地3 ひだまり館内

<コンディショニング>
・コンディショニング整体
・スポーツ整体
・美容整体
・自律神経調整
・インソール作成

<boby work>
・ペルカボード
・ピラティス
・ヨガ etc…
希望イメージ
シンプル 複雑
単色 カラフル
暗い 明るい
日常 高級
遊び心 厳粛
未来的 伝統的
女性的 男性的
希望する色
青系、水色系、黄・オレンジ系
納品ファイル
補足説明
■ 選んだ理由

デザインと印象が良かったです!

■ 提案者全員のお礼・コメント

皆様、お忙しい中ご協力いただきありがとうございました。

```html
<!DOCTYPE html>
<html lang="ja">
<head>
<meta charset="utf-8">
<title>バランスRスタジオ 名刺</title>
<link rel="stylesheet" href="https://fonts.googleapis.com/css2?family=Noto+Sans+JP:wght@400;500;700&family=Noto+Serif+JP:wght@600;700&display=swap">
<style>
  :root {
    --page: #e4e4e4;
    --card: #ffffff;
    --ink: #2b2b2b;
    --blue: #1f78c1;
    --navy: #1d4f7a;
    --teal: #7ecccc;
    --teal-deep: #5fbcbc;
    --yellow: #f4c21b;
    --orange: #ef8a1e;
    --sky: #5ab3e6;
    --sans: "Noto Sans JP", sans-serif;
    --serif: "Noto Serif JP", serif;
  }
  * { margin: 0; padding: 0; box-sizing: border-box; }
  html, body { width: 805px; height: 1200px; overflow: hidden; background: var(--page); }
  body { position: relative; font-family: var(--sans); color: var(--ink); }

  .card {
    position: absolute; left: 57px; width: 692px; height: 483px;
    background: var(--card); overflow: hidden;
    box-shadow: 0 2px 6px rgba(0,0,0,.18);
  }
  .card--front { top: 80px; }
  .card--back { top: 643px; }

  /* front */
  .brand { position: absolute; left: 34px; top: 56px; display: flex; align-items: center; gap: 12px; }
  .brand__dot { width: 40px; height: 40px; border-radius: 50%; background: var(--sky); }
  .brand__name { font-size: 38px; font-weight: 700; color: var(--blue); letter-spacing: .5px; }
  .tagline {
    position: absolute; left: 282px; top: 62px;
    font-family: var(--serif); font-weight: 700; font-size: 22px; color: var(--blue); letter-spacing: 1px;
  }
  .rep { position: absolute; left: 110px; top: 168px; font-size: 14px; }
  .person { position: absolute; left: 110px; top: 186px; display: flex; align-items: baseline; gap: 12px; }
  .person__name { font-size: 32px; font-weight: 500; letter-spacing: 4px; }
  .person__roman { font-size: 13px; }
  .tel { position: absolute; left: 110px; top: 240px; display: flex; align-items: center; gap: 8px; font-size: 19px; }
  .icon { width: 20px; height: 20px; flex: none; }
  .rule {
    position: absolute; left: 0; top: 306px; width: 692px; height: 6px;
    background: linear-gradient(90deg, var(--orange), var(--yellow) 40%, var(--sky) 75%, var(--blue));
  }
  .studio { position: absolute; left: 54px; top: 330px; font-size: 21px; font-weight: 500; letter-spacing: 1px; }
  .info { position: absolute; left: 54px; display: flex; align-items: center; gap: 8px; font-size: 15px; }
  .info--address { top: 376px; }
  .info--mail { top: 410px; }
  .figure-front {
    position: absolute; left: 548px; top: 112px; width: 118px; height: 200px; border-radius: 50px 50px 10px 10px;
    background: linear-gradient(180deg, #f6d24a, #f2a13d 45%, #7cc6c4);
    opacity: .7;
  }

  /* back */
  .back-field { position: absolute; inset: 0; }
  .menu { position: absolute; left: 36px; top: 40px; width: 240px; text-align: center; color: #fff; font-size: 16px; line-height: 1.7; }
  .menu__head { color: var(--navy); font-weight: 700; font-size: 17px; }
  .menu__group + .menu__group { margin-top: 26px; border-top: 1px solid rgba(255,255,255,.7); padding-top: 20px; }
  .menu__list { list-style: none; }
  .back-brand { position: absolute; left: 285px; top: 138px; width: 150px; text-align: center; color: #fff; }
  .back-brand__dot { width: 86px; height: 86px; border-radius: 50%; background: #fff; opacity: .9; margin: 0 auto 18px; }
  .back-brand__name { font-size: 30px; font-weight: 700; }
  .figure-back {
    position: absolute; left: 470px; top: 50px; width: 200px; height: 390px; border-radius: 60px;
    background: linear-gradient(160deg, #f3b84a, #e8743a 50%, #79c4c2);
    opacity: .55;
  }
</style>
</head>
<body>

<section class="card card--front">
  <div class="brand">
    <span class="brand__dot"></span>
    <span class="brand__name">R studio</span>
  </div>
  <p class="tagline">楽しくキレイと健康を手に入れる</p>

  <p class="rep">代表者</p>
  <p class="person"><span class="person__name">野村 拓海</span><span class="person__roman">Takumi Nomura</span></p>
  <p class="tel">
    <svg class="icon" viewBox="0 0 20 20"><rect x="3" y="1" width="14" height="18" rx="3" fill="var(--sky)"/><rect x="6" y="4" width="8" height="10" fill="#fff"/></svg>
    090−8472−6615
  </p>

  <div class="figure-front" role="img" aria-label="カラフルな線で描いた体を伸ばす人物のイラスト"></div>

  <div class="rule"></div>

  <p class="studio">バランスRスタジオ</p>
  <p class="info info--address">
    <svg class="icon" viewBox="0 0 20 20"><rect width="20" height="20" rx="3" fill="var(--sky)"/><path d="M5 5h10M5 8h10M10 8v8" stroke="#fff" stroke-width="2"/></svg>
    329-0412 栃木県下野市緑ヶ丘412番地3 ひだまり館内
  </p>
  <p class="info info--mail">
    <svg class="icon" viewBox="0 0 20 20"><rect width="20" height="20" rx="3" fill="var(--sky)"/><rect x="4" y="6" width="12" height="9" fill="none" stroke="#fff" stroke-width="1.6"/><path d="M4 6l6 5 6-5" fill="none" stroke="#fff" stroke-width="1.6"/></svg>
    balance.r.studio@hoshimail.jp
  </p>
</section>

<section class="card card--back">
  <svg class="back-field" viewBox="0 0 692 483" preserveAspectRatio="none">
    <path d="M0 0H520C430 90 420 390 500 483H0Z" fill="var(--teal)"/>
  </svg>

  <div class="menu">
    <div class="menu__group">
      <p class="menu__head">&lt;コンディショニング&gt;</p>
      <ul class="menu__list">
        <li>・コンディショニング整体</li>
        <li>・スポーツ整体</li>
        <li>・美容整体</li>
        <li>・自律神経調整</li>
        <li>・インソール作成</li>
      </ul>
    </div>
    <div class="menu__group">
      <p class="menu__head">&lt;boby work&gt;</p>
      <ul class="menu__list">
        <li>・ペルカボード</li>
        <li>・ピラティス</li>
        <li>・ヨガ　etc…</li>
      </ul>
    </div>
  </div>

  <div class="back-brand">
    <div class="back-brand__dot"></div>
    <p class="back-brand__name">R studio</p>
  </div>

  <div class="figure-back" role="img" aria-label="ヨガやストレッチのポーズをとる線画の人物たち"></div>
</section>

</body>
</html>
```